Complete redesign of site for leading equipment supplier and service company

Looking for a new website design to portray our offerings for customers. Bay & Gate is a distributor, installer and service provider for loading dock equipment and industrial doors. We are a factory authorized dealer for a number of top brand names and also provide service after the sale on our equipment as well as competitors equipment. We are also in the midst of developing a service program tied to a QR coding system that would need to be incorporated in the website where a customer can scan a QR code and be brought to a specific "Service Request" portal that would be a form they could fill out to send to our service department.
Site should also feature product information pages for our base of product offerings, a completed projects area where we can showcase the work we've done, and a bio area for our sales and management team.

Some information for research:

Our Products That We Sell:

marlowvantix.com
pendrastolvik.com
zqrgates.com
lvmsupply.com
https://www.hobart-quill.com/commercial-doors
https://www.pemblagates.com/
https://www.ulngates.com/

Similar Companies and Competitors:

http://www.brisquelgear.com/
https://www.tidewaybaysupply.com/
https://www.orbitgearworks.com/
https://www.lumbrakastel.com/
https://velmar.quenrobin.com/en/us?gclid=XkpQRTmwzab4CSCCFjxbjC_QXJMF1mYZn9XCwUmzqSisqQL_kmLnd-vzfgJJCrGuw4DjGnHtd9ryrDwolRBw_CxCF

Target Market(s)

Existing and potential customers throughout the greater New England region including:
Manufacturing
Distribution
Cold Storage
Pharmaceutical
Food Production
Beverage Bottling
Warehousing

Coding

Number of Pages Required

Colors
9ccb3b
ecf7fb

Requirements
Must have
• Home Page
Product Page
Service Page
Contact Page
Separate page that will be directed to from a QR code that we will supply to specific customers

```html
<!DOCTYPE html>
<html lang="en">
<head>
<meta charset="utf-8">
<title>Bay &amp; Gate — Loading Dock Equipment &amp; Industrial Doors</title>
<link href="https://fonts.googleapis.com/css2?family=Montserrat:wght@400;500;600;800;900&family=Rufina:wght@400;700&family=Lato:ital,wght@0,400;0,700;1,400&display=swap" rel="stylesheet">
<style>
:root{
  --green:#9dc764;
  --green-soft:#c9dfa8;
  --green-deep:#2c5219;
  --ink:#1d1d1d;
  --muted:#8a8a8a;
  --card:#f7f7f7;
  --line:#e6e6e6;
  --black:#000;
  --white:#fff;
}
*{box-sizing:border-box;margin:0;padding:0}
html,body{width:1200px;height:3759px;overflow:hidden;background:var(--white)}
body{position:relative;font-family:"Lato",sans-serif;color:var(--ink)}
.abs{position:absolute}

/* header & hero */
.hero{left:0;top:0;width:1200px;height:676px;background:linear-gradient(160deg,#5a5d5b 0%,#3e403f 45%,#232423 100%)}
.hero::after{content:"";position:absolute;inset:0;background:rgba(0,0,0,.25)}
.brand-tab{left:160px;top:0;width:98px;height:88px;background:var(--white);border-radius:0 0 22px 22px;display:flex;align-items:center;justify-content:center;z-index:3}
.brand-name{font-family:"Montserrat",sans-serif;font-weight:800;font-size:15px;line-height:1.05;text-align:center;color:var(--green-deep)}
.nav{left:518px;top:36px;display:flex;gap:32px;z-index:3;font-family:"Montserrat",sans-serif;font-size:11px;letter-spacing:.4px;color:var(--white)}
.nav a{color:inherit;text-decoration:none;position:relative}
.nav a.active{color:var(--green)}
.nav a.active::after{content:"";position:absolute;left:50%;top:20px;margin-left:-5px;border:5px solid transparent;border-bottom:7px solid var(--green);border-top:0}
.search{left:828px;top:36px;z-index:3}
.req-btn{left:866px;top:26px;width:173px;height:38px;background:var(--green);color:var(--white);z-index:3;display:flex;align-items:center;font-family:"Montserrat",sans-serif;font-size:11px;font-weight:500;letter-spacing:.3px}
.req-btn .ico{width:26px;height:26px;background:var(--white);margin:0 12px 0 6px;display:flex;align-items:center;justify-content:center}
.hero-title{left:0;top:222px;width:1200px;text-align:center;font-family:"Montserrat",sans-serif;font-weight:900;font-size:51px;line-height:60px;z-index:3;letter-spacing:.5px}
.hero-title .g{color:var(--green)}
.hero-title .w{color:var(--white)}
.hero-text{left:360px;top:357px;width:480px;text-align:center;font-style:italic;font-size:12px;line-height:22px;color:var(--white);z-index:3}
.btn{background:var(--green);color:var(--white);font-family:"Montserrat",sans-serif;font-size:12.5px;font-weight:500;letter-spacing:.3px;display:flex;align-items:center;justify-content:center;z-index:3}
.hero-btn{left:536px;top:428px;width:128px;height:44px}
.slide-arrow{width:38px;height:38px;border-radius:50%;background:rgba(255,255,255,.22);top:318px;z-index:3;display:flex;align-items:center;justify-content:center}

/* headings */
.sec-title{font-family:"Rufina",serif;font-size:35px;color:var(--ink);z-index:1}
.sec-title .dot{position:absolute;left:-6px;top:-4px;width:44px;height:44px;border-radius:50%;background:var(--green);z-index:-1}
.body-text{font-size:10.5px;line-height:19.5px;color:var(--muted)}

/* framed photo */
.framed{}
.framed .frame{position:absolute;border:4px solid var(--green);border-radius:48px 0 48px 48px}
.framed .photo{position:absolute;border-radius:0 48px 48px 48px}

/* services */
.svc{top:1209px;width:271px;height:352px;background:var(--card);border-radius:6px;overflow:hidden}
.svc .photo{position:absolute;left:0;top:0;width:271px;height:180px}
.svc .badge{position:absolute;left:107px;top:147px;width:56px;height:56px;background:var(--green);display:flex;align-items:center;justify-content:center}
.svc h3{position:absolute;left:0;top:222px;width:271px;text-align:center;font-family:"Montserrat",sans-serif;font-weight:500;font-size:19px;color:var(--ink)}
.svc p{position:absolute;left:18px;top:261px;width:235px;text-align:center;font-size:10.2px;line-height:19px;color:var(--muted)}
.svc .corner{position:absolute;right:0;bottom:0;width:0;height:0;border-left:44px solid transparent;border-bottom:44px solid var(--green-deep)}
.svc .corner-arrow{position:absolute;right:7px;bottom:6px}

/* products */
.filters{left:163px;top:1748px;display:flex;font-family:"Montserrat",sans-serif;font-size:12.5px;color:#444;letter-spacing:.3px}
.filters span.sep{margin:0 24px;color:#555}
.filters .on{color:var(--green)}
.pager{top:1735px;width:30px;height:30px;display:flex;align-items:center;justify-content:center}

/* request banner */
.banner{left:160px;top:2755px;width:878px;height:277px;border-radius:10px;background:linear-gradient(90deg,#4a4c4c 0%,#6a6c6c 50%,#4a4b4b 100%);overflow:hidden}
.banner::after{content:"";position:absolute;inset:0;background:rgba(0,0,0,.3)}
.banner h2{position:absolute;left:0;top:44px;width:878px;text-align:center;font-family:"Rufina",serif;font-weight:400;font-size:35px;color:var(--white);z-index:2}
.banner p{position:absolute;left:190px;top:109px;width:498px;text-align:center;font-size:11.5px;line-height:21px;color:var(--white);z-index:2}
.banner .btn{position:absolute;left:376px;top:173px;width:128px;height:44px}

/* partners */
.partners-rule{left:160px;top:3080px;width:878px;height:1px;background:var(--line)}
.partners-title{left:0;top:3092px;width:1200px;text-align:center;font-family:"Rufina",serif;font-size:19px;font-weight:700;color:var(--ink)}
.partner{top:3146px;width:136px;height:61px;background:var(--white);box-shadow:0 0 6px rgba(0,0,0,.08);display:flex;align-items:center;justify-content:center;font-family:"Montserrat",sans-serif;font-weight:600;font-size:13px;color:#333}

/* footer */
.footer{left:0;top:3273px;width:1200px;height:486px;background:var(--black)}
.f-head{top:3332px;font-family:"Rufina",serif;font-size:15px;color:var(--green)}
.f-text{font-size:10.2px;line-height:22.5px;color:#d8d8d8}
.f-text b{color:var(--green);font-weight:400}
.f-links{list-style:none;font-size:10.2px;line-height:22.5px;color:#d8d8d8}
.f-links li::before{content:"- ";color:#888}
.f-input{left:702px;width:336px;height:37px;background:var(--white);font-size:10px;color:#555;padding:0 12px;display:flex;align-items:center}
.f-send{left:702px;top:3461px;width:75px;height:36px;font-size:12px}
.f-rule{top:3580px;height:1px;background:#3a3a3a}
.f-logo{left:571px;top:3548px;width:58px;height:64px;background:var(--black);border:2px solid var(--white);border-radius:6px;display:flex;align-items:center;justify-content:center}
.f-logo .brand-name{color:var(--white);font-size:10px}
.copyright{left:0;top:3638px;width:1200px;text-align:center;font-size:10.2px;color:#cfcfcf}
.social{top:3673px;width:29px;height:29px;background:var(--green)}
</style>
</head>
<body>

<!-- Hero -->
<div class="abs hero" role="img" aria-label="Warehouse interior with steel staircase and mezzanine"></div>
<div class="abs brand-tab"><span class="brand-name">BAY<br>&amp;<br>GATE</span></div>
<nav class="abs nav">
  <a class="active" href="#">HOME</a><a href="#">PRODUCT</a><a href="#">SERVICES</a><a href="#">CONTACT</a>
</nav>
<svg class="abs search" width="16" height="16" viewBox="0 0 16 16" aria-label="Search"><circle cx="6.5" cy="6.5" r="5" fill="none" stroke="#9dc764" stroke-width="1.6"/><line x1="10.3" y1="10.3" x2="14.5" y2="14.5" stroke="#9dc764" stroke-width="1.8"/></svg>
<div class="abs req-btn"><span class="ico"><svg width="14" height="14" viewBox="0 0 14 14"><path d="M2 12 L8 6" stroke="#2c5219" stroke-width="2.2" stroke-linecap="round"/><circle cx="9.5" cy="4.5" r="3" fill="none" stroke="#2c5219" stroke-width="1.8"/></svg></span>SERVICES REQUEST</div>

<h1 class="abs hero-title"><span class="g">BAY &amp; GATE</span><br><span class="w">IN NEW ENGLAND</span></h1>
<p class="abs hero-text">Lorem ipsum dolor sit amet, consectetur adipiscing elit, sed do eiusmod tempor incididunt ut labore et dolore quis nostrud exercitation ullamco laboris nisi ut aliquip.</p>
<div class="abs btn hero-btn">CONTACT US</div>
<div class="abs slide-arrow" style="left:141px"><svg width="10" height="10" viewBox="0 0 10 10"><path d="M6.5 1.5 L3 5 L6.5 8.5" fill="none" stroke="#fff" stroke-width="1.3"/></svg></div>
<div class="abs slide-arrow" style="left:1019px"><svg width="10" height="10" viewBox="0 0 10 10"><path d="M3.5 1.5 L7 5 L3.5 8.5" fill="none" stroke="#fff" stroke-width="1.3"/></svg></div>

<!-- Welcome -->
<div class="abs framed" style="left:160px;top:750px;width:323px;height:323px">
  <div class="frame" style="left:0;top:23px;width:302px;height:300px"></div>
  <div class="photo" role="img" aria-label="Bright warehouse interior with mezzanine office" style="left:23px;top:0;width:300px;height:300px;background:linear-gradient(135deg,#eef0f0 0%,#cfd3d5 55%,#9aa0a2 100%)"></div>
</div>
<h2 class="abs sec-title" style="left:576px;top:744px"><span class="dot"></span>Welcome To Bay &amp; Gate</h2>
<p class="abs body-text" style="left:563px;top:806px;width:470px">Lorem ipsum dolor sit amet, consectetur adipiscing elit, sed do eiusmod tempor incididunt ut labore et dolore magna aliqua. Ut enim ad minim veniam, quis nostrud exercitation ullamco laboris nisi ut aliquip ex ea commodo consequat. Duis aute irure dolor in reprehenderit in voluptate velit esse cillum dolore eu fugiat nulla pariatur. Excepteur sint occaecat cupidatat non proident, sunt in culpa qui officia deserunt mollit anim id est laborum</p>
<p class="abs body-text" style="left:563px;top:918px;width:470px">Lorem ipsum dolor sit amet, consectetur adipiscing elit, sed do eiusmod tempor incididunt ut labore et dolore magna aliqua. Ut enim ad minim veniam, quis nostrud exercitation ullamco laboris nisi ut aliquip ex ea commodo consequat.</p>
<div class="abs btn" style="left:562px;top:1006px;width:127px;height:44px">LEARN MORE</div>

<!-- Services -->
<h2 class="abs sec-title" style="left:178px;top:1129px"><span class="dot" style="left:-18px"></span>Our Services</h2>

<div class="abs svc" style="left:160px">
  <div class="photo" role="img" aria-label="Technician installing a white door panel" style="background:linear-gradient(135deg,#c7cdbf,#f0f0ee 55%,#a99a80)"></div>
  <div class="badge"><svg width="26" height="28" viewBox="0 0 26 28"><rect x="5" y="3" width="16" height="22" fill="none" stroke="#fff" stroke-width="1.6"/><line x1="2" y1="25" x2="24" y2="25" stroke="#fff" stroke-width="1.6"/><circle cx="17" cy="14" r="1.3" fill="#fff"/></svg></div>
  <h3>Installation</h3>
  <p>Lorem ipsum dolor sit amet, consectetur adipiscing elit, sed do eiusmod tempor incididunt ut labore et dolore magna aliqua.</p>
  <div class="corner"></div>
  <svg class="corner-arrow" width="12" height="12" viewBox="0 0 12 12"><path d="M2 6 H10 M7 3 L10 6 L7 9" fill="none" stroke="#fff" stroke-width="1.2"/></svg>
</div>
<div class="abs svc" style="left:464px">
  <div class="photo" role="img" aria-label="Technician repairing a sliding window door" style="background:linear-gradient(135deg,#7f8a78,#e6e8e6 55%,#c9c4bc)"></div>
  <div class="badge"><svg width="26" height="28" viewBox="0 0 26 28"><rect x="8" y="8" width="10" height="8" fill="none" stroke="#fff" stroke-width="1.6"/><line x1="10" y1="3" x2="10" y2="8" stroke="#fff" stroke-width="1.6"/><line x1="16" y1="3" x2="16" y2="8" stroke="#fff" stroke-width="1.6"/><path d="M13 16 V21 H21" fill="none" stroke="#fff" stroke-width="1.6"/></svg></div>
  <h3>Repair</h3>
  <p>Lorem ipsum dolor sit amet, consectetur adipiscing elit, sed do eiusmod tempor incididunt ut labore et dolore magna aliqua.</p>
  <div class="corner"></div>
  <svg class="corner-arrow" width="12" height="12" viewBox="0 0 12 12"><path d="M2 6 H10 M7 3 L10 6 L7 9" fill="none" stroke="#fff" stroke-width="1.2"/></svg>
</div>
<div class="abs svc" style="left:768px">
  <div class="photo" role="img" aria-label="Technician servicing an overhead garage door" style="background:linear-gradient(135deg,#b59474,#e4e4e2 50%,#8c98ab)"></div>
  <div class="badge"><svg width="26" height="24" viewBox="0 0 26 24"><rect x="3" y="7" width="20" height="13" rx="2" fill="none" stroke="#fff" stroke-width="1.6"/><path d="M9 7 V4 H17 V7" fill="none" stroke="#fff" stroke-width="1.6"/><line x1="3" y1="13" x2="23" y2="13" stroke="#fff" stroke-width="1.4"/></svg></div>
  <h3>Maintenance</h3>
  <p>Lorem ipsum dolor sit amet, consectetur adipiscing elit, sed do eiusmod tempor incididunt ut labore et dolore magna aliqua.</p>
  <div class="corner"></div>
  <svg class="corner-arrow" width="12" height="12" viewBox="0 0 12 12"><path d="M2 6 H10 M7 3 L10 6 L7 9" fill="none" stroke="#fff" stroke-width="1.2"/></svg>
</div>

<!-- Products -->
<h2 class="abs sec-title" style="left:178px;top:1617px"><span class="dot" style="left:-18px"></span>Our Products</h2>
<p class="abs body-text" style="left:162px;top:1677px;width:625px">Lorem ipsum dolor sit amet, consectetur adipiscing elit, sed do eiusmod tempor incididunt ut labore et dolore magna aliqua. Ut enim ad minim veniam, quis nostrud exercitation ullamco laboris nisi ut aliquip ex ea commodo consequat.</p>
<div class="abs filters"><span class="on">ALL DOORS</span><span class="sep">|</span><span>HIGH SPEED DOORS</span><span class="sep">|</span><span>ROLLING DOORS</span><span class="sep">|</span><span>SECTIONAL DOORS</span></div>
<div class="abs pager" style="left:971px;background:var(--green-soft)"><svg width="10" height="10" viewBox="0 0 10 10"><path d="M6.5 1.5 L3 5 L6.5 8.5" fill="none" stroke="#2c5219" stroke-width="1.4"/></svg></div>
<div class="abs pager" style="left:1009px;background:var(--green)"><svg width="10" height="10" viewBox="0 0 10 10"><path d="M3.5 1.5 L7 5 L3.5 8.5" fill="none" stroke="#1d3a10" stroke-width="1.4"/></svg></div>

<!-- product grid: row 1 -->
<div class="abs framed" style="left:160px;top:1801px;width:256px;height:256px">
  <div class="frame" style="left:0;top:16px;width:240px;height:240px"></div>
  <div class="photo" role="img" aria-label="Red high speed roll-up door in a warehouse" style="left:16px;top:0;width:240px;height:240px;background:linear-gradient(135deg,#9ea3a5,#c6463e 45%,#b9bcbc 80%)"></div>
</div>
<div class="abs framed" style="left:472px;top:1801px;width:256px;height:256px">
  <div class="frame" style="left:0;top:16px;width:240px;height:240px"></div>
  <div class="photo" role="img" aria-label="White sectional door with windows" style="left:16px;top:0;width:240px;height:240px;background:linear-gradient(135deg,#c9ccce,#eceded 50%,#a6a9ab)"></div>
</div>
<div class="abs framed" style="left:784px;top:1801px;width:256px;height:256px">
  <div class="frame" style="left:0;top:16px;width:240px;height:240px"></div>
  <div class="photo" role="img" aria-label="Distribution center exterior with row of loading docks" style="left:16px;top:0;width:240px;height:240px;background:linear-gradient(180deg,#9fb9d6 0%,#dfe5ea 45%,#b7b9ba 100%)"></div>
</div>
<!-- row 2 -->
<div class="abs framed" style="left:160px;top:2121px;width:256px;height:256px">
  <div class="frame" style="left:0;top:16px;width:240px;height:240px"></div>
  <div class="photo" role="img" aria-label="Warehouse with white sectional doors" style="left:16px;top:0;width:240px;height:240px;background:linear-gradient(135deg,#8e9396,#dcdfe0 50%,#9a9d9e)"></div>
</div>
<div class="abs framed" style="left:472px;top:2121px;width:256px;height:256px">
  <div class="frame" style="left:0;top:16px;width:240px;height:240px"></div>
  <div class="photo" role="img" aria-label="Long warehouse hall with rolling doors and blue dock plates" style="left:16px;top:0;width:240px;height:240px;background:linear-gradient(135deg,#6f7477,#c5c9cb 50%,#4f6ea0)"></div>
</div>
<div class="abs framed" style="left:784px;top:2121px;width:256px;height:256px">
  <div class="frame" style="left:0;top:16px;width:240px;height:240px"></div>
  <div class="photo" role="img" aria-label="Clean room corridor with blue high speed door" style="left:16px;top:0;width:240px;height:240px;background:linear-gradient(135deg,#dfe3e4,#f0f1f1 50%,#5a6fb0)"></div>
</div>
<!-- row 3 -->
<div class="abs framed" style="left:160px;top:2432px;width:256px;height:256px">
  <div class="frame" style="left:0;top:16px;width:240px;height:240px"></div>
  <div class="photo" role="img" aria-label="Dark blue garage door in a white building" style="left:16px;top:0;width:240px;height:240px;background:linear-gradient(135deg,#eef0f1,#2a3447 45%,#9fa3a5)"></div>
</div>
<div class="abs framed" style="left:472px;top:2432px;width:256px;height:256px">
  <div class="frame" style="left:0;top:16px;width:240px;height:240px"></div>
  <div class="photo" role="img" aria-label="Loading dock doors with yellow bumpers" style="left:16px;top:0;width:240px;height:240px;background:linear-gradient(180deg,#7a4b4c 0%,#e9e9e8 30%,#cfcfca 100%)"></div>
</div>
<div class="abs framed" style="left:784px;top:2432px;width:256px;height:256px">
  <div class="frame" style="left:0;top:16px;width:240px;height:240px"></div>
  <div class="photo" role="img" aria-label="Grey roller shutter doors in an industrial hall" style="left:16px;top:0;width:240px;height:240px;background:linear-gradient(135deg,#3e4342,#8f9a89 50%,#5b605f)"></div>
</div>

<!-- Service request banner -->
<div class="abs banner">
  <div role="img" aria-label="Technicians in hard hats working on an overhead door" style="position:absolute;inset:0"></div>
  <h2>Submit a Service Request</h2>
  <p>Lorem ipsum dolor sit amet, consectetur adipiscing elit, sed do eiusmod tempor incididunt ullamco laboris nisi ut aliquip ex ea commodo consequat.</p>
  <div class="btn">GET IN TOUCH</div>
</div>

<!-- Partners -->
<div class="abs partners-rule"></div>
<h3 class="abs partners-title">Our Partners</h3>
<div class="abs partner" style="left:168px">Pendrastolvik</div>
<div class="abs partner" style="left:313px">Hobart-Quill</div>
<div class="abs partner" style="left:458px">Pembla</div>
<div class="abs partner" style="left:604px">Marlowvantix</div>
<div class="abs partner" style="left:749px">LVM Supply</div>
<div class="abs partner" style="left:895px">ZQR Gates</div>

<!-- Footer -->
<footer class="abs footer"></footer>
<h4 class="abs f-head" style="left:162px">Location</h4>
<p class="abs f-text" style="left:162px;top:3363px;width:180px">123, Address, State Name, Street Name, City Name, Zipcode</p>
<p class="abs f-text" style="left:162px;top:3408px"><b>P</b> - 123.456.7890</p>
<p class="abs f-text" style="left:162px;top:3431px"><b>E</b> - info@bayandgate.com</p>

<h4 class="abs f-head" style="left:388px">Links</h4>
<ul class="abs f-links" style="left:388px;top:3363px"><li>Home</li><li>Products</li><li>Services</li><li>Contact</li></ul>
<ul class="abs f-links" style="left:524px;top:3363px"><li>Help</li><li>Employee Login</li><li>Privacy Policy</li><li>Terms &amp; Condition</li></ul>

<h4 class="abs f-head" style="left:702px">Sign Up Newsletter</h4>
<div class="abs f-input" style="top:3371px">Name * :</div>
<div class="abs f-input" style="top:3416px">Email * :</div>
<div class="abs btn f-send">SEND</div>

<div class="abs f-rule" style="left:160px;width:403px"></div>
<div class="abs f-rule" style="left:637px;width:401px"></div>
<div class="abs f-logo"><span class="brand-name">BAY<br>&amp;<br>GATE</span></div>
<p class="abs copyright">Copyright © BAY &amp; GATE NEW ENGLAND - 2020 . All Right Reserved.</p>
<div class="abs social" role="img" aria-label="Social link" style="left:529px"></div>
<div class="abs social" role="img" aria-label="Social link" style="left:567px"></div>
<div class="abs social" role="img" aria-label="Social link" style="left:605px"></div>
<div class="abs social" role="img" aria-label="Social link" style="left:643px"></div>

</body>
</html>
```